Quillivant CD cover

Cd cover for new album called "Velvet Harbour". The band is called "Quillivant". I want it to include the image below and maybe some neon pink as well. Not a big fan of clean lines. Hope that helps!

Colors
E54698
E96AAD
F1A4CE
F9D9EA
FCEFF6

```html
<!DOCTYPE html>
<html lang="en">
<head>
<meta charset="utf-8">
<title>Quillivant — Velvet Harbour CD Artwork</title>
<link rel="stylesheet" href="https://fonts.googleapis.com/css2?family=Lobster+Two:ital,wght@1,700&family=Orbitron:wght@700&family=Montserrat:wght@500&family=Advent+Pro:wght@200&family=Share+Tech+Mono&display=swap">
<style>
  :root {
    --stage: #2b2b2b;
    --aqua: #b3fbf6;
    --art-light: #d2fffb;
    --art-mid: #5fe0d7;
    --art-deep: #2fc7bf;
    --art-warm: #b4f09a;
    --pink: #e96aad;
    --pink-neon: #e54698;
    --white: #ffffff;
    --band-shade: #d8d8d8;
    --hub-light: #e0e0e0;
    --hub-dark: #858585;
    --rim: #4a4a4a;
  }
  * { margin: 0; padding: 0; box-sizing: border-box; }
  html, body { width: 864px; height: 1200px; overflow: hidden; background: var(--stage); }
  .sheet { position: relative; width: 864px; height: 1200px; }

  .cover { position: absolute; left: 82px; width: 336px; height: 336px; background: var(--aqua); overflow: hidden; }
  .disc { position: absolute; left: 447px; width: 336px; height: 336px; overflow: visible; }
  .row-one { top: 60px; }
  .row-two { top: 425px; }
  .row-three { top: 804px; }

  .artwork {
    position: absolute;
    background: linear-gradient(125deg, var(--art-light) 0%, var(--art-mid) 38%, var(--art-deep) 62%, var(--art-mid) 80%, var(--art-warm) 100%);
  }

  .band-pink { position: absolute; left: 0; width: 100%; background: var(--pink); display: flex; align-items: center; justify-content: center; }
  .band-light {
    position: absolute; left: 0; width: 100%;
    background: linear-gradient(90deg, var(--band-shade), var(--white) 50%, var(--band-shade));
    display: flex; align-items: center; justify-content: center;
  }
  .title-script {
    font-family: "Lobster Two", cursive;
    font-weight: 700; font-style: italic;
    font-size: 32px; line-height: 1; color: var(--white);
  }
  .title-sans {
    position: absolute; left: 0; width: 100%; text-align: center;
    font-family: "Montserrat", sans-serif; font-weight: 500;
    font-size: 22px; letter-spacing: 1.6px; color: var(--pink);
  }
  .title-thin {
    font-family: "Advent Pro", sans-serif; font-weight: 200;
    font-size: 32px; line-height: 1; color: var(--pink);
  }
  .artist-block {
    position: absolute; left: 0; width: 100%; text-align: center;
    font-family: "Orbitron", sans-serif; font-weight: 700;
    font-size: 11.5px; letter-spacing: 1.6px; color: var(--pink);
  }
  .artist-mono {
    position: absolute; left: 0; width: 100%; text-align: center;
    font-family: "Share Tech Mono", monospace;
    font-size: 16px; letter-spacing: 3px; color: var(--white);
  }
</style>
</head>
<body>
<main class="sheet">

  <svg width="0" height="0" style="position:absolute" aria-hidden="true">
    <defs>
      <linearGradient id="art-fill" x1="0" y1="0" x2="1" y2="1">
        <stop offset="0" stop-color="#d2fffb"/>
        <stop offset="0.38" stop-color="#5fe0d7"/>
        <stop offset="0.62" stop-color="#2fc7bf"/>
        <stop offset="0.8" stop-color="#5fe0d7"/>
        <stop offset="1" stop-color="#b4f09a"/>
      </linearGradient>
      <radialGradient id="hub-metal" cx="50%" cy="35%" r="65%">
        <stop offset="0" stop-color="#e0e0e0"/>
        <stop offset="1" stop-color="#858585"/>
      </radialGradient>
      <linearGradient id="light-band" x1="0" x2="1">
        <stop offset="0" stop-color="#d8d8d8"/>
        <stop offset="0.5" stop-color="#ffffff"/>
        <stop offset="1" stop-color="#d8d8d8"/>
      </linearGradient>
      <clipPath id="disc-face"><circle cx="168" cy="168" r="166"/></clipPath>
    </defs>
  </svg>

  <!-- Version one: script title on pink band -->
  <section class="cover row-one">
    <div class="artwork" style="left:46px; top:42px; width:243px; height:149px;" role="img" aria-label="Scribbled neon-outlined crocodile-like creature drawing"></div>
    <div class="band-pink" style="top:225px; height:43px;"><span class="title-script">Velvet Harbour</span></div>
    <div class="artist-block" style="top:280px;">QUILLIVANT</div>
  </section>

  <svg class="disc row-one" viewBox="0 0 336 336" aria-label="Disc label, version one">
    <g clip-path="url(#disc-face)">
      <rect width="336" height="336" fill="var(--aqua)"/>
      <rect x="85" y="23" width="141" height="84" fill="url(#art-fill)" role="img" aria-label="Scribbled neon-outlined crocodile-like creature drawing"/>
      <rect x="0" y="225" width="336" height="43" fill="var(--pink)"/>
      <text x="168" y="256" text-anchor="middle" font-family="'Lobster Two', cursive" font-weight="700" font-style="italic" font-size="32" fill="var(--white)">Velvet Harbour</text>
      <text x="168" y="293" text-anchor="middle" font-family="Orbitron, sans-serif" font-weight="700" font-size="11.5" letter-spacing="1.6" fill="var(--pink)">QUILLIVANT</text>
    </g>
    <circle cx="168" cy="168" r="166" fill="none" stroke="var(--rim)" stroke-width="1.2"/>
    <circle cx="168" cy="168" r="50" fill="none" stroke="#777" stroke-width="0.8"/>
    <circle cx="168" cy="168" r="46" fill="url(#hub-metal)"/>
    <circle cx="168" cy="168" r="30" fill="var(--stage)"/>
  </svg>

  <!-- Version two: title above, large artwork below -->
  <section class="cover row-two">
    <div class="title-sans" style="top:49px;">VELVET HARBOUR</div>
    <div class="artist-block" style="top:86px;">QUILLIVANT</div>
    <div class="artwork" style="left:0; top:112px; width:336px; height:224px;" role="img" aria-label="Large scribbled neon-outlined crocodile-like creature drawing"></div>
  </section>

  <svg class="disc row-two" viewBox="0 0 336 336" aria-label="Disc label, version two">
    <defs>
      <path id="title-arc" d="M 40 142 A 130 130 0 0 1 296 142"/>
    </defs>
    <g clip-path="url(#disc-face)">
      <rect width="336" height="336" fill="var(--aqua)"/>
      <rect x="53" y="136" width="283" height="182" fill="url(#art-fill)" role="img" aria-label="Large scribbled neon-outlined crocodile-like creature drawing"/>
      <text font-family="Montserrat, sans-serif" font-weight="500" font-size="24" letter-spacing="2.5" fill="var(--pink)">
        <textPath href="#title-arc" startOffset="50%" text-anchor="middle">VELVET HARBOUR</textPath>
      </text>
      <text x="168" y="90" text-anchor="middle" font-family="Orbitron, sans-serif" font-weight="700" font-size="11.5" letter-spacing="1.6" fill="var(--pink)">QUILLIVANT</text>
    </g>
    <circle cx="168" cy="168" r="166" fill="none" stroke="var(--rim)" stroke-width="1.2"/>
    <circle cx="168" cy="168" r="50" fill="none" stroke="#777" stroke-width="0.8"/>
    <circle cx="168" cy="168" r="46" fill="url(#hub-metal)"/>
    <circle cx="168" cy="168" r="30" fill="var(--stage)"/>
  </svg>

  <!-- Version three: artwork on top, light and pink bands below -->
  <section class="cover row-three">
    <div class="artwork" style="left:24px; top:0; width:312px; height:225px;" role="img" aria-label="Scribbled neon-outlined crocodile-like creature drawing"></div>
    <div class="band-light" style="top:225px; height:45px;"><span class="title-thin">VELVET HARBOUR</span></div>
    <div class="band-pink" style="top:270px; height:66px;"></div>
    <div class="artist-mono" style="top:279px;">Quillivant</div>
  </section>

  <svg class="disc row-three" viewBox="0 0 336 336" aria-label="Disc label, version three">
    <g clip-path="url(#disc-face)">
      <rect width="336" height="336" fill="var(--aqua)"/>
      <rect x="11" y="21" width="299" height="167" fill="url(#art-fill)" role="img" aria-label="Scribbled neon-outlined crocodile-like creature drawing"/>
      <rect x="0" y="224" width="336" height="43" fill="url(#light-band)"/>
      <rect x="0" y="267" width="336" height="69" fill="var(--pink)"/>
      <text x="168" y="257" text-anchor="middle" font-family="'Advent Pro', sans-serif" font-weight="200" font-size="32" fill="var(--pink)">VELVET HARBOUR</text>
      <text x="168" y="293" text-anchor="middle" font-family="'Share Tech Mono', monospace" font-size="16" letter-spacing="3" fill="var(--white)">Quillivant</text>
    </g>
    <circle cx="168" cy="168" r="166" fill="none" stroke="var(--rim)" stroke-width="1.2"/>
    <circle cx="168" cy="168" r="50" fill="none" stroke="#777" stroke-width="0.8"/>
    <circle cx="168" cy="168" r="46" fill="url(#hub-metal)"/>
    <circle cx="168" cy="168" r="30" fill="var(--stage)"/>
  </svg>

</main>
</body>
</html>
```